We are looking for a new website design for our SEO WEB Development Company. The URL is www.brellowcreativeworks.com

We want it to be a more powerful representation of what we do. We are also looking for a number of designers that we will give continuous business to every month. The persons design we choose will also get a proposal to complete 4 - 6 new designs for us every month for our clients.

Be creative as you can in your design submissions. We really want to stand out!

Just to give you an idea of what we like look at this site: http://www.tovandigitalstudio.com/

```html
<!DOCTYPE html>
<html lang="en">
<head>
<meta charset="utf-8">
<title>Brellow Interactive Group – Media Marketing Experts</title>
<link href="https://fonts.googleapis.com/css2?family=Arimo:wght@400;700&family=Tinos:wght@400;700&display=swap" rel="stylesheet">
<style>
:root{
  --black:#000;
  --ink:#0c0c0c;
  --panel:#1b1b1b;
  --orange:#e8720f;
  --orange-deep:#c9560a;
  --cyan:#2fb7e6;
  --link-blue:#6aa8e8;
  --brand-ink:#222;
  --white:#fff;
  --grey-text:#8d8d8d;
  --tab-light:#c9bfa6;
  --tab-dark:#6f6650;
  --green:#4cc43c;
}
*{box-sizing:border-box;margin:0;padding:0}
html,body{width:911px;height:1200px;overflow:hidden;background:var(--black)}
body{position:relative;font-family:"Arimo",Arial,sans-serif;color:var(--white)}
.abs{position:absolute}

.topbar{left:0;top:0;width:911px;height:40px;background:linear-gradient(#3a3a3a,#111 60%,#000)}
.search-field{left:738px;top:9px;width:136px;height:20px;background:var(--white);border:1px solid #999}
.search-button{left:880px;top:7px;width:25px;height:23px;background:linear-gradient(#8ef07a,var(--green));border:1px solid #2a7a20;border-radius:3px}

.header{left:0;top:40px;width:911px;height:91px;background:var(--white)}
.brand{left:16px;top:62px;display:flex;align-items:center;gap:8px}
.brand-square{width:16px;height:16px;background:var(--orange)}
.brand-name{font-family:"Arimo",Arial,sans-serif;font-weight:700;font-size:24px;color:var(--brand-ink);line-height:1;white-space:nowrap}

.nav{left:331px;top:103px;width:580px;height:28px;background:#0b0b0b;border-top-left-radius:6px;display:flex;align-items:center}
.nav a{color:var(--cyan);font-size:12px;text-decoration:none;padding:0 6px;border-right:1px solid #555}
.nav a:first-child{padding-left:18px}
.nav .contact{margin-left:auto;padding-right:8px;font-size:10.5px;font-weight:700;color:var(--white)}

.hero-strip{left:0;top:131px;width:911px;height:20px;background:linear-gradient(#555,#222)}
.hero{left:0;top:151px;width:911px;height:169px;background:linear-gradient(var(--orange),var(--orange-deep))}
.hero-tagline{right:6px;top:156px;text-align:left;font-weight:700;font-size:15.5px;line-height:19px;text-shadow:1px 1px 2px #000}
.hero-title{left:32px;top:200px;font-weight:700;font-size:40px;letter-spacing:.3px}
.hero-skyline{left:527px;top:196px;width:384px;height:124px;background:linear-gradient(#d9cdb8,#8f8578 55%,#3b3630);clip-path:polygon(20% 0,100% 0,100% 100%,0 100%)}

.main{left:0;top:320px;width:911px;height:340px;background:var(--ink)}
.intro{left:42px;top:322px;width:276px;font-size:7.4px;line-height:8.6px;color:#ddd}
.intro p{margin-bottom:6px}
.intro b{font-family:"Tinos",serif;color:var(--link-blue);font-size:8.6px}

.quote{left:320px;top:320px;width:416px;height:340px;background:var(--panel)}
.quote h2{position:absolute;left:5px;top:30px;font-family:"Tinos",serif;font-size:17px;font-weight:700;border-bottom:2px solid var(--cyan);padding-bottom:4px;width:405px}
.quote p{position:absolute;left:5px;top:60px;width:405px;font-size:12.4px;line-height:14.2px}
.services{left:323px;top:573px;width:413px;height:85px;background:#050505;border:1px solid #2a2a2a}
.services h3{position:absolute;left:6px;top:6px;font-size:9.5px;font-weight:700}
.services h3 span{color:#e0482a}
.services ul{position:absolute;list-style:none;font-size:6px;line-height:12px;color:#888;text-transform:uppercase}
.services li::before{content:"› ";color:#aaa}

.form{left:740px;top:320px;width:171px;height:340px;background:var(--ink)}
.form label{position:absolute;left:7px;font-size:12px;font-weight:700}
.form .field{position:absolute;left:7px;width:158px;height:19px;background:var(--white);border:1px solid #888}
.form .submit{position:absolute;left:7px;width:158px;height:23px;border-radius:4px;background:linear-gradient(#6fc6ff,#1c78d6);font-size:10.5px;font-weight:700;text-align:center;line-height:23px}

.band{left:0;top:660px;width:911px;height:340px;background:linear-gradient(#2a2a2a,#111)}
.follow{left:40px;top:671px;width:384px;height:208px;background:#3b3930}
.follow-title{left:43px;top:675px;font-size:10px;font-weight:700}
.tab{position:absolute;top:671px;width:51px;height:208px;background:linear-gradient(90deg,var(--tab-dark),var(--tab-light) 50%,var(--tab-dark));border-left:1px solid #222}
.tab .icon{position:absolute;left:6px;top:46px;width:38px;height:38px;border-radius:8px}
.tab span{position:absolute;left:17px;top:150px;transform:rotate(-90deg);transform-origin:left top;font-size:7.5px;white-space:nowrap}
.showcase{left:424px;top:667px;width:484px;height:333px;background:var(--white)}
.showcase-line{font-size:19px;color:#222;letter-spacing:.5px;position:absolute}
.showcase-line em{font-style:normal;color:#1a9ad6}
.showcase-photo{left:424px;top:730px;width:484px;height:270px;background:linear-gradient(#efefef,#9c9c9c 60%,#2b2b2b)}

.share-bar{left:0;top:1000px;width:911px;height:34px;background:#050505;font-size:9px;font-weight:700}
.share-bar .share{position:absolute;left:88px;top:11px}
.share-bar .share i{display:inline-block;width:9px;height:9px;background:#3b5998;margin-right:4px;vertical-align:-1px}
.share-bar .call{position:absolute;left:361px;top:10px;font-size:9.5px}

.footer{left:0;top:1034px;width:911px;height:166px;background:linear-gradient(#181818,#050505)}
.footer-col{position:absolute;top:16px}
.footer-col h4{color:var(--cyan);font-size:9.4px;font-weight:700;margin-bottom:12px}
.footer-col li{list-style:none;font-size:8.4px;line-height:9.5px;color:var(--grey-text)}
.copyright{right:16px;bottom:3px;font-size:6.5px;color:#aaa}
</style>
</head>
<body>

<div class="abs topbar"></div>
<div class="abs search-field"></div>
<div class="abs search-button">
  <svg width="23" height="21" viewBox="0 0 23 21"><circle cx="10" cy="9" r="5" fill="none" stroke="#fff" stroke-width="2"/><line x1="14" y1="13" x2="18" y2="17" stroke="#fff" stroke-width="2.5"/></svg>
</div>

<div class="abs header"></div>
<div class="abs brand">
  <span class="brand-square"></span>
  <span class="brand-name">Brellow Interactive Group</span>
</div>

<nav class="abs nav">
  <a>Creative Design</a><a>Website Design</a><a>Internet Marketing</a><a style="border:none">IT Consulting</a>
  <span class="contact">Contact us 877-555-0142</span>
</nav>

<div class="abs hero-strip"></div>
<div class="abs hero"></div>
<div class="abs hero-skyline" role="img" aria-label="City skyline at dusk"></div>
<div class="abs hero-tagline">Focusing on your brand<br>With the right Internet Marketing tools</div>
<div class="abs hero-title">Media Marketing Experts</div>

<div class="abs main"></div>
<div class="abs intro">
  <p><b>Brellow Interactive Group</b> is a leading Dallas Web Site Design, Publishing and Internet Marketing Firm. Our Dallas Texas based Website Design and Internet Marketing experts are some of the best in the industry!</p>
  <p><b>Brellow Interactive Web</b> is a full-service Dallas based Advertising Agency comprised of experienced advertising and marketing professionals that provide clients with a clear and distinct voice in the marketplace. Web Site Design and Internet Marketing experts at our Dallas location specialize in developing Online Marketing Strategies, Search Engine Marketing and Optimization (SEO), Pay Per Click, Web Site Design and Development, and Online Reputation Management.</p>
  <p><b>Brellow Interactive Publishing</b> provides full-service custom publishing and consulting services for magazines, newsletters, blogs and web sites. We are the complete interactive publishing arm for your organization. Our services include: Strategic Planning and Computer Modeling; Art Direction and Design; Production Services; Circulation Marketing and Management; Subscription Fulfillment Management; Advertising Sales Management; Web Site and Digital Magazine Design and Management; and Video Streaming Services.</p>
  <p><b>Brellow Interactive Media</b> provides cost-effective Web Site Design services, Search Engine Marketing, Internet Advertising, Internet Marketing Campaigns and most important, we can accommodate any budget.</p>
  <p><b>Brellow Interactive Reputation Management and Repair</b> provides reputation management and repair services to the online community. We offer a plan of action to create a process of tracking an entity's actions and other entities' opinions about those actions; reporting on those actions and opinions; and reacting to that report creating a feedback loop. Reputation management has become essential with the advent of widespread computing. Reputation management systems use predefined criteria for processing complex data to report the many factors affecting a company's reputation. However, these systems only facilitate and automate the process of determining trustworthiness.</p>
</div>

<section class="abs quote">
  <h2>Get A Free Reputation Management &amp; Repair Quote!</h2>
  <p>The goal of a reputation management or repair campaign is to create and/or strengthen an authoritative, positive image of your company by helping you gain positive name recognition across a wide range of websites. Most Search Engine users only pay attention to the Top 20 results, which is what we focus on. We will work closely with you to come up with a strong, detailed plan to put you at the top of search engins such as Searchly.com and above the negative listings about you. We will analyze your situation closely and create a detailed but flexible plan for your Reputation Management Campaign.</p>
</section>

<div class="abs services">
  <h3>PRODUCTS &amp; <span>SERVICES</span></h3>
  <ul style="left:10px;top:20px"><li>Fleets</li><li>Commercial</li><li>Wholesale</li><li>Individual and Automotive</li></ul>
  <ul style="left:122px;top:20px"><li>Medium Truck</li><li>Specialty Tires</li><li>Loaders</li><li>Individual and Automotive</li></ul>
  <ul style="left:234px;top:20px"><li>Medium Truck</li><li>Specialty Tires</li><li>Loaders</li><li>Individual and Automotive</li></ul>
</div>

<form class="abs form">
  <label style="top:24px">Name</label><div class="field" style="top:40px"></div>
  <label style="top:81px">Phone Number</label><div class="field" style="top:97px"></div>
  <label style="top:129px">Email</label><div class="field" style="top:145px"></div>
  <label style="top:178px">Website &nbsp;Address</label><div class="field" style="top:194px"></div>
  <div class="submit" style="top:225px">Request For &nbsp;Quote</div>
</form>

<div class="abs band"></div>
<div class="abs follow"></div>
<div class="tab" style="left:40px"><div class="icon" style="background:#9a3bb8"></div><span>Bookmarks</span></div>
<div class="tab" style="left:94px"><div class="icon" style="background:#2a9fd8"></div><span>Chirper</span></div>
<div class="tab" style="left:148px"><div class="icon" style="background:#e06a1c"></div><span>Foxfire</span></div>
<div class="tab" style="left:202px"><div class="icon" style="background:#3366b0"></div><span>Friendbook</span></div>
<div class="tab" style="left:256px"><div class="icon" style="background:#8cc63f"></div><span>Wanderup</span></div>
<div class="tab" style="left:310px"><div class="icon" style="background:#6cbf2a"></div><span>Delve</span></div>
<div class="tab" style="left:364px;width:60px"><div class="icon" style="background:#d83a2a"></div><span>RSS</span></div>
<div class="abs follow-title">Follow us on</div>

<div class="abs showcase">
  <div class="showcase-line" style="left:4px;top:8px">NOT ONLY <em>BRELLOW.</em></div>
  <div class="showcase-line" style="left:120px;top:31px">BUT <em>SOLUTIONS.</em></div>
</div>
<div class="abs showcase-photo" role="img" aria-label="Business team reviewing documents around a laptop in an office"></div>

<div class="abs share-bar">
  <span class="share"><i></i>Share on Friendbook</span>
  <span class="call">Call us for a quote today: 214-555-0187</span>
</div>

<footer class="abs footer">
  <div class="footer-col" style="left:32px"><h4>Creative Design</h4><ul><li>Creative Advertising</li><li>Print Design</li><li>Corporate Identity</li><li>Packaging</li></ul></div>
  <div class="footer-col" style="left:176px"><h4>Internet Marketing Services</h4><ul><li>Search Engine Optimization</li><li>Pay-per-Click Campaign Consulting</li><li>Email Marketing</li><li>SEO Copywriting</li><li>Reputation Management</li></ul></div>
  <div class="footer-col" style="left:361px"><h4>Website Design</h4><ul><li>Web Design</li><li>E-commerce</li><li>Multimedia</li><li>Web Application Development</li></ul></div>
  <div class="footer-col" style="left:500px"><h4>IT Consulting Brellow Interactive</h4><ul><li>About Us</li><li>Our Work</li><li>Contact Us</li></ul></div>
  <div class="abs copyright">Copyright 2011 Brellow Interactive Group reserved all rights</div>
</footer>

</body>
</html>
```